Invitation Design Project

50th Birthday Party for Tim. Big, loud party planned with loads of friends and family. at our home. Decorations will be coloured lanterns attached to the pergola and hired a band.

Details:

on 19th October, 2013
(other details when design chosen)
at: 7.00 pm
RSVP: 14th October, 2013

```html
<!DOCTYPE html>
<html lang="en">
<head>
<meta charset="utf-8">
<title>Tim's 50th Birthday Invitation</title>
<link rel="stylesheet" href="https://fonts.googleapis.com/css2?family=Sorts+Mill+Goudy:ital@0;1&display=swap">
<style>
  :root {
    --paper: #f8f5e8;
    --rose: #e2185e;
    --royal: #0a0ae6;
    --lantern-warm: #f6d9a8;
    --lantern-cool: #cfe6f2;
    --lantern-pink: #f3c6d6;
  }
  html, body {
    margin: 0;
    padding: 0;
    overflow: hidden;
    background: var(--paper);
  }
  .invitation {
    position: relative;
    width: 849px;
    height: 1200px;
    overflow: hidden;
    background: var(--paper);
    font-family: "Sorts Mill Goudy", Georgia, serif;
    color: var(--rose);
  }
  .lantern-garland {
    position: absolute;
    left: 0;
    top: 0;
    width: 849px;
    height: 415px;
    background: linear-gradient(180deg,
      var(--lantern-cool) 0%,
      var(--lantern-pink) 45%,
      var(--lantern-warm) 80%,
      var(--paper) 100%);
  }
  .line {
    position: absolute;
    left: 0;
    width: 100%;
    margin: 0;
    text-align: center;
    line-height: 1;
    white-space: nowrap;
  }
  .greeting { font-style: italic; font-size: 36px; }
  .guest-name {
    font-style: italic;
    font-size: 110px;
    color: var(--royal);
  }
  .age-line { font-style: italic; font-size: 35px; }
  .age-number { color: var(--royal); font-size: 46px; }
  .detail { font-size: 40px; }
  .detail-italic { font-style: italic; font-size: 40px; }
</style>
</head>
<body>
  <main class="invitation">
    <div class="lantern-garland" role="img" aria-label="Strings of colourful paper lanterns hanging across the top of the invitation"></div>

    <p class="line greeting" style="top:400px">Its a great Celebration !!</p>
    <p class="line greeting" style="top:448px">Please join us for food and fun</p>
    <p class="line greeting" style="top:495px">in honour of</p>

    <h1 class="line guest-name" style="top:560px;font-weight:400">Tim</h1>

    <p class="line age-line" style="top:690px">who is turning <span class="age-number">50</span>!</p>

    <p class="line detail" style="top:767px">On 19th October, 2013</p>
    <p class="line detail" style="top:812px">at 7:00 p.m.</p>

    <p class="line detail" style="top:909px">0000 Any Street west</p>
    <p class="line detail-italic" style="top:959px">Townsvlle , ST&nbsp; 0000</p>

    <p class="line detail-italic" style="top:1053px">RSVP by 14th October, 2013</p>
    <p class="line detail-italic" style="top:1104px">phone 000 000 000</p>
  </main>
</body>
</html>
```